resleeving

we need a revamped flyer to email to our existing customers

ensure all spelling is correct

if using sentences make sure to use centre margins

```html
<!DOCTYPE html>
<html lang="en">
<head>
<meta charset="utf-8">
<title>Stainless Steel Resleeving – Summit Auto Works</title>
<link rel="stylesheet" href="https://fonts.googleapis.com/css2?family=Days+One&family=Open+Sans:wght@400;700;800&family=Oswald:wght@500;600&display=swap">
<style>
  :root {
    --yellow: #f7d90a;
    --black: #0b0b0b;
    --white: #ffffff;
    --red: #e3262b;
    --stage: #d9dcdb;
    --metal-light: #8d8f90;
    --metal-dark: #3a3b3c;
  }
  * { margin: 0; padding: 0; box-sizing: border-box; }
  html, body { width: 1200px; height: 800px; overflow: hidden; background: var(--stage); }
  .canvas { position: relative; width: 1200px; height: 800px; }

  .flyer {
    position: absolute; left: 332px; top: 21px;
    width: 1064px; height: 1505px;
    transform: scale(0.5037); transform-origin: 0 0;
    background: var(--yellow); overflow: hidden;
    font-family: "Open Sans", Arial, sans-serif; color: var(--black);
  }
  .flyer-shapes { position: absolute; inset: 0; width: 1064px; height: 1505px; }

  .brand-mark {
    position: absolute; left: 0; top: 300px; width: 490px;
    text-align: center; font-weight: 700; font-size: 34px; letter-spacing: 0.5px;
  }
  .title {
    position: absolute; left: 490px; top: 72px; width: 520px;
    text-align: center; color: var(--white);
    font-family: "Days One", Arial, sans-serif; font-size: 60px; line-height: 76px;
  }
  .question {
    position: absolute; left: 440px; top: 328px; width: 580px;
    text-align: center; font-family: "Days One", Arial, sans-serif;
    font-size: 62px; line-height: 66px;
  }
  .benefits {
    position: absolute; left: 420px; top: 500px; width: 640px;
    list-style: none; text-align: center; font-size: 34px; line-height: 52px;
  }
  .benefits li::before { content: "-\00a0\00a0"; }
  .benefits .key { font-weight: 800; }

  .part-photo {
    position: absolute; border-radius: 18px;
    background: radial-gradient(ellipse at 40% 40%, var(--metal-light), var(--metal-dark));
  }
  .part-hero { left: 135px; top: 510px; width: 225px; height: 250px; border-radius: 40px 40px 30px 30px; }
  .part-1 { left: 35px; top: 765px; width: 178px; height: 130px; }
  .part-2 { left: 293px; top: 770px; width: 197px; height: 115px; border-radius: 50px; }
  .part-3 { left: 573px; top: 765px; width: 212px; height: 130px; border-radius: 40px; }
  .part-4 { left: 860px; top: 765px; width: 185px; height: 125px; border-radius: 30px; }

  .aim {
    position: absolute; left: 30px; top: 938px; width: 1004px;
    text-align: center; color: var(--yellow);
    font-family: "Oswald", "Arial Narrow", sans-serif; font-weight: 600;
    font-size: 64px; line-height: 70px; transform: scaleX(0.86);
  }
  .free-phone {
    position: absolute; left: 740px; top: 1170px; width: 280px;
    text-align: center; color: var(--white); white-space: nowrap;
    font-family: "Oswald", "Arial Narrow", sans-serif; font-weight: 500;
    font-size: 32px; line-height: 40px; transform: rotate(-15deg);
  }
  .free-phone strong { font-weight: 600; font-size: 36px; }

  .footer-mark {
    position: absolute; left: 120px; top: 1372px; width: 245px;
    text-align: center; font-weight: 700; font-size: 20px;
  }
  .contact {
    position: absolute; left: 380px; top: 1240px;
    font-style: normal; font-size: 28px; line-height: 40px;
  }
  .contact-name { font-weight: 700; font-size: 38px; line-height: 50px; }
  .contact .label { color: var(--yellow); }
  .contact .value { font-weight: 700; }
  .contact .sep { color: var(--yellow); }
  .website {
    position: absolute; left: 0; top: 1428px; width: 1064px;
    text-align: center; color: var(--yellow);
    font-family: "Days One", Arial, sans-serif; font-size: 38px; letter-spacing: 12px;
  }
</style>
</head>
<body>
<main class="canvas">
  <article class="flyer">
    <svg class="flyer-shapes" viewBox="0 0 1064 1505" aria-hidden="true">
      <rect class="band-top" x="0" y="0" width="1064" height="262" fill="var(--black)"/>
      <rect class="band-rule" x="0" y="262" width="1064" height="13" fill="var(--white)"/>
      <rect class="band-aim" x="0" y="830" width="1064" height="372" fill="var(--black)"/>
      <g class="scallops" fill="var(--yellow)">
        <circle cx="120" cy="800" r="140"/>
        <circle cx="400" cy="800" r="140"/>
        <circle cx="675" cy="800" r="140"/>
        <circle cx="945" cy="800" r="140"/>
      </g>
      <rect class="band-contact" x="0" y="1202" width="1064" height="208" fill="var(--white)"/>
      <rect class="band-web" x="0" y="1410" width="1064" height="95" fill="var(--black)"/>
      <circle class="brand-disc" cx="245" cy="222" r="250" fill="var(--white)"/>
      <circle class="brand-dot" cx="245" cy="190" r="80" fill="var(--yellow)"/>
      <circle class="footer-dot" cx="242" cy="1300" r="52" fill="var(--yellow)"/>
      <polygon class="starburst" transform="translate(880 1210) rotate(-15)" fill="var(--red)" stroke="var(--white)" stroke-width="4"
        points="125,0 106,21.1 115.5,47.9 89.8,60 88.4,88.4 60,89.8 47.9,115.5 21.1,106 0,125 -21.1,106 -47.9,115.5 -60,89.8 -88.4,88.4 -89.8,60 -115.5,47.9 -106,21.1 -125,0 -106,-21.1 -115.5,-47.9 -89.8,-60 -88.4,-88.4 -60,-89.8 -47.9,-115.5 -21.1,-106 0,-125 21.1,-106 47.9,-115.5 60,-89.8 88.4,-88.4 89.8,-60 115.5,-47.9 106,-21.1"/>
    </svg>

    <div class="brand-mark">SUMMIT AUTO WORKS</div>

    <h1 class="title">Stainless Steel<br>Resleeving</h1>

    <h2 class="question">Why re-sleeve<br>your cylinders?</h2>
    <ul class="benefits">
      <li>Cost effective</li>
      <li>Longer lasting</li>
      <li>No waiting for overseas parts</li>
      <li class="key">Re-manufacturing = Re-cycling</li>
      <li>Cylinders are no longer available</li>
    </ul>

    <div class="part-photo part-hero" role="img" aria-label="Photo of a cast iron brake cylinder assembly"></div>
    <div class="part-photo part-1" role="img" aria-label="Photo of a resleeved cylinder housing seen from the bore"></div>
    <div class="part-photo part-2" role="img" aria-label="Photo of a wheel cylinder"></div>
    <div class="part-photo part-3" role="img" aria-label="Photo of a brake booster cylinder"></div>
    <div class="part-photo part-4" role="img" aria-label="Photo of a master cylinder with reservoir"></div>

    <p class="aim">Our aim is to have your parts<br>repaired with the quickest turn-around<br>times possible</p>

    <div class="footer-mark">SUMMIT AUTO WORKS</div>
    <address class="contact">
      <div class="contact-name">Summit Auto Works</div>
      <div>18 Ridgeway Road Hamilton</div>
      <div><span class="label">Ph:</span> <span class="value">07 555 0142</span> <span class="sep">|</span> <span class="label">Fax:</span> <span class="value">07 555 0143</span></div>
      <div class="value">Email: parts@summitautoworks.co.nz</div>
    </address>

    <p class="free-phone">Free Phone:<br><strong>0800 55 01 44</strong></p>

    <div class="website">www.summitautoworks.co.nz</div>
  </article>
</main>
</body>
</html>
```